Marrowind Unified Care Brochures (2)

We need two brochures about whiplash treatment to be designed. One is for referring physicians, the other is for the patients they refer. I'd like a few design elements to tie the two together, but also have them be easily distinguishable from one another.
In our region we are considered the top soft tissue injury clinic. We are trying to increase the awareness of our referring physicians to the fact that we have an exceptional rate of success treating acceleration/deceleration injuries from motor vehicle accidents.
We understand the emotional toll of whiplash. We understand how pain robs people of their vitality and motivation. We help victims of whiplash reclaim their health and vitality.
We use Quickleafpress.com for our printing.
Logo, trifold brochure template, and text(pdf files) have been up;oaded to this project.
The text we have provided is what we want. There are two versions of it. One is for the brochure for patients, and one is for the brochure for doctors.

Target Market(s)

Physicians that will refer Whiplash victims to our clinic for soft tissue injury treatment.

Industry/Entity Type

Health

Font styles to use
Serif

Requirements
Must have
• professional graphics that compliment the text.
• All AI files, graphic files etc.
• Colors that work with the Logo.
• Fonts for company name can be found on our website: www.marrowindunifiedcare.example
Nice to have
• We'd like it to have a nice visual flow. We have only provided the text we want. Titles can be different if the design choices would make sense with better titles. We want it to be convincing and calming, and project our sensitivity to those suffering and also prject our confidence in our long history of curing the condition.

```html
<!DOCTYPE html>
<html lang="en">
<head>
<meta charset="utf-8">
<title>Marrowind Unified Care – Trifold Brochure</title>
<link href="https://fonts.googleapis.com/css2?family=Cinzel:wght@600&family=Open+Sans:wght@400;700&display=swap" rel="stylesheet">
<style>
  :root {
    --page-bg: #e9e4dc;
    --navy: #243f78;
    --brand-blue: #1a7fc4;
    --cyan: #2aa7df;
    --teal-name: #1a8fbf;
    --skin-light: #e9b996;
    --skin-mid: #c98e6c;
    --skin-dark: #8a5a45;
    --white: #ffffff;
  }
  html, body {
    margin: 0;
    width: 1200px;
    height: 1200px;
    overflow: hidden;
    background: var(--page-bg);
    font-family: "Open Sans", Arial, sans-serif;
  }
  .brochure {
    position: absolute;
    left: 72px;
    top: 190px;
    width: 1056px;
    height: 820px;
    background: var(--white);
    box-shadow: 0 6px 18px rgba(0,0,0,0.25);
    overflow: hidden;
  }
  .brochure-art {
    position: absolute;
    inset: 0;
  }
  .panel-text {
    position: absolute;
    color: var(--white);
    text-align: center;
  }
  .about-panel {
    left: 0;
    width: 346px;
    top: 398px;
  }
  .about-block { margin-bottom: 20px; }
  .about-block h2 {
    margin: 0;
    font-size: 18.5px;
    line-height: 20px;
    font-weight: 700;
  }
  .about-block p {
    margin: 0 auto;
    width: 290px;
    font-size: 13.3px;
    line-height: 16px;
  }
  .contact-panel {
    left: 346px;
    width: 352px;
    top: 676px;
    font-size: 14px;
    line-height: 20px;
  }
  .contact-panel h3 {
    margin: 0;
    font-size: 14px;
    font-weight: 700;
  }
  .contact-panel p { margin: 0; }
  .contact-web {
    margin-top: 20px !important;
    font-weight: 700;
  }
  .tagline {
    position: absolute;
    right: 26px;
    top: 22px;
    margin: 0;
    text-align: right;
    color: var(--white);
    font-size: 25px;
    line-height: 30px;
  }
  .brand-mark {
    position: absolute;
    left: 798px;
    top: 516px;
    width: 176px;
    height: 176px;
    border-radius: 50%;
    background: var(--cyan);
  }
  .brand-name {
    position: absolute;
    left: 698px;
    width: 358px;
    top: 730px;
    margin: 0;
    text-align: center;
    color: var(--teal-name);
    font-family: "Cinzel", Georgia, serif;
    font-size: 29px;
    line-height: 33px;
    font-weight: 600;
    letter-spacing: 0.5px;
  }
</style>
</head>
<body>
<div class="brochure">
  <svg class="brochure-art" viewBox="0 0 1056 820" width="1056" height="820">
    <defs>
      <linearGradient id="leftPhoto" x1="0" y1="0" x2="0" y2="1">
        <stop offset="0" stop-color="#f3ece6"/>
        <stop offset="0.2" stop-color="var(--skin-mid)"/>
        <stop offset="0.45" stop-color="var(--skin-dark)"/>
        <stop offset="0.62" stop-color="var(--navy)"/>
        <stop offset="1" stop-color="var(--navy)"/>
      </linearGradient>
      <linearGradient id="midTopPhoto" x1="0" y1="0" x2="1" y2="0.4">
        <stop offset="0" stop-color="#3c3d44"/>
        <stop offset="0.45" stop-color="#6e6468"/>
        <stop offset="1" stop-color="var(--skin-light)"/>
      </linearGradient>
      <linearGradient id="rightPhoto" x1="0" y1="0" x2="1" y2="1">
        <stop offset="0" stop-color="#f2c9aa"/>
        <stop offset="0.6" stop-color="var(--skin-light)"/>
        <stop offset="1" stop-color="var(--skin-mid)"/>
      </linearGradient>
      <linearGradient id="midBottomPhoto" x1="0" y1="0" x2="0" y2="1">
        <stop offset="0" stop-color="#c8d2dc"/>
        <stop offset="0.35" stop-color="#8a9db3"/>
        <stop offset="0.7" stop-color="var(--brand-blue)"/>
        <stop offset="1" stop-color="var(--brand-blue)"/>
      </linearGradient>
      <linearGradient id="midBottomSide" x1="0" y1="0" x2="1" y2="0">
        <stop offset="0" stop-color="rgba(255,255,255,0)"/>
        <stop offset="0.75" stop-color="rgba(255,255,255,0)"/>
        <stop offset="1" stop-color="rgba(120,180,220,0.45)"/>
      </linearGradient>
      <linearGradient id="topBand" x1="0" y1="0" x2="1" y2="1">
        <stop offset="0" stop-color="#1b74b8"/>
        <stop offset="1" stop-color="#0a95d0"/>
      </linearGradient>
    </defs>

    <rect x="0" y="0" width="346" height="820" fill="url(#leftPhoto)" role="img" aria-label="Photo of a therapist's hands massaging a patient's back, fading into navy"/>

    <rect x="346" y="0" width="352" height="480" fill="url(#midTopPhoto)" role="img" aria-label="Close-up photo of a patient's shoulder during massage"/>
    <rect x="698" y="0" width="358" height="560" fill="url(#rightPhoto)" role="img" aria-label="Photo of hands working on a patient's upper back"/>

    <path d="M448 0 C600 20 880 110 1056 282 L1056 0 Z" fill="url(#topBand)"/>
    <path d="M448 0 C600 20 880 110 1056 282" fill="none" stroke="#223f7d" stroke-width="7"/>
    <path d="M448 -6 C600 14 860 96 1010 228" fill="none" stroke="#4cc3f0" stroke-width="3" opacity="0.7"/>

    <path d="M346 454 Q520 400 698 426 Q900 440 1056 522 L1056 820 L698 820 Z" fill="var(--white)"/>
    <path d="M346 454 Q520 400 698 426 L698 820 L346 820 Z" fill="url(#midBottomPhoto)" role="img" aria-label="Photo of a cyclist in a red jersey riding against a cloudy sky"/>
    <rect x="346" y="420" width="352" height="400" fill="url(#midBottomSide)"/>
    <path d="M346 454 Q520 400 698 426 Q900 440 1056 522" fill="none" stroke="var(--cyan)" stroke-width="9"/>

    <line x1="698" y1="0" x2="698" y2="426" stroke="rgba(255,255,255,0.25)" stroke-width="1"/>
  </svg>

  <section class="panel-text about-panel">
    <div class="about-block">
      <h2>Making a Difference<br>in Marrowind With Massage</h2>
      <p>Local area physicians know that we offer the highest quality medical massage available for injury &amp; pain treatment, which is why they have been entrusting their patients to us for over 19 years.</p>
    </div>
    <div class="about-block">
      <h2>Experience Matters and<br>Our Numbers are Strong</h2>
      <p>We have over 120 years of injury, stress, and pain relief experience. Over 130,000 hours of clinical “hands on” healing makes Marrowind Unified Care’s reputation for highly effective treatment second to none.</p>
    </div>
    <div class="about-block">
      <h2>Become Pain Free and<br>Improve your Health</h2>
      <p>Whether you have been injured in a car accident, on the job, while playing sports or if your pain is caused by repetitive motion or emotional stress – massage therapy can bring you lasting relief.</p>
    </div>
  </section>

  <section class="panel-text contact-panel">
    <h3>Contact Us</h3>
    <p>TEL: 555.010.4821 | FAX: (555)010-4822</p>
    <p>4410 Harbor Crest Way NE Suite 12 Marrowind<br>WA 98000</p>
    <p class="contact-web">www.marrowindunifiedcare.example</p>
  </section>

  <p class="tagline">To heal.<br>To educate.<br>To empower.</p>

  <div class="brand-mark"></div>
  <h1 class="brand-name">Marrowind Unified<br>Care</h1>
</div>
</body>
</html>
```